BRISKWAY ELECTRICAL SIGN

We are wanting a sign to mount on the side of the road to attract peoples attention, it will be 1200mm high by 2400mm wide. We want it to stand out from the others, modern sharp looking, We are an electrical contractor who wants to be the market leader and supplier of choice to our current clients and futre clients.

Industry/Entity Type

Electrical

Colors

Designer to choose colors to be used in the design.

Requirements
Must have
• Name: Briskway Electrical
• Our logo as per uploaded files
• The words: Design - Installation - Maintenance
• Freecall: 0800 342 958
• Mobile : 021 736 4192 (delete mobile number if gets to cluttered)
• Web: www.briskway.net.nz
Should not have
• a light bulb, or plug

```html
<!DOCTYPE html>
<html lang="en">
<head>
<meta charset="utf-8">
<title>Briskway Electrical – Roadside Sign</title>
<link rel="stylesheet" href="https://fonts.googleapis.com/css2?family=Audiowide&family=Montserrat:wght@600;700&display=swap">
<style>
  :root {
    --backdrop: #222b00;
    --sign-white: #ffffff;
    --brand-blue: #3d74bd;
    --panel-blue: #4e7cbf;
    --brand-green: #a9cf38;
    --ink: #333333;
  }
  * { margin: 0; padding: 0; box-sizing: border-box; }
  html, body {
    width: 1200px;
    height: 923px;
    overflow: hidden;
    background: var(--backdrop);
  }
  .sign {
    position: absolute;
    left: 164px;
    top: 243px;
    width: 871px;
    height: 436px;
    background: var(--sign-white);
    overflow: hidden;
  }
  .sign__panel {
    position: absolute;
    left: 0;
    top: 0;
    width: 871px;
    height: 436px;
  }
  .brand-name {
    position: absolute;
    right: 28px;
    top: 58px;
    text-align: right;
    font-family: "Montserrat", sans-serif;
    font-weight: 700;
    color: var(--brand-blue);
    line-height: 1;
  }
  .brand-name__main {
    display: block;
    font-size: 66px;
    letter-spacing: 1px;
  }
  .brand-name__sub {
    display: block;
    font-size: 40px;
    margin-top: 6px;
    letter-spacing: 1px;
  }
  .brand-name__dot {
    display: inline-block;
    width: 18px;
    height: 18px;
    border-radius: 50%;
    background: var(--brand-blue);
    margin-right: 12px;
    vertical-align: middle;
  }
  .services {
    position: absolute;
    right: 28px;
    top: 188px;
    font-family: "Audiowide", sans-serif;
    font-size: 17.5px;
    letter-spacing: 0.4px;
    color: var(--brand-green);
    white-space: nowrap;
  }
  .contact {
    position: absolute;
    right: 28px;
    top: 262px;
    text-align: right;
    font-family: "Montserrat", sans-serif;
    font-weight: 600;
    font-size: 31px;
    color: var(--ink);
    line-height: 47px;
  }
  .web {
    position: absolute;
    right: 28px;
    top: 400px;
    font-family: "Montserrat", sans-serif;
    font-weight: 600;
    font-size: 21px;
    letter-spacing: 3px;
    color: var(--brand-green);
  }
</style>
</head>
<body>
  <main class="sign">
    <svg class="sign__panel" viewBox="0 0 871 436" aria-hidden="true">
      <path d="M0 0 H330 C200 70 170 280 360 436 H0 Z" fill="var(--panel-blue)"/>
      <path d="M330 0 C200 70 170 280 360 436" fill="none" stroke="var(--sign-white)" stroke-width="4"/>
    </svg>

    <h1 class="brand-name">
      <span class="brand-name__main"><span class="brand-name__dot"></span>BRISKWAY</span>
      <span class="brand-name__sub">ELECTRICAL</span>
    </h1>

    <p class="services">DESIGN - INSTALLATION - MAINTENANCE</p>

    <div class="contact">
      <p class="contact__line">Freecall: 0800 342 958</p>
      <p class="contact__line">Mobile : 021 736 4192</p>
    </div>

    <p class="web">www.briskway.net.nz</p>
  </main>
</body>
</html>
```